Illustrated restaurant promotional posters

We need series of 5 promotional posters for a restaurant, each one promoting a different special across the week. The text for each poster must be included and is in the file attached to this brief, but the design should only be treated as a draft idea for what we are looking for (we are flexible). We're looking to add illustrations to these posters, which may or may not require a complete re-imagining. The restaurant serves American BBQ with a latin twist, is smart casual, and the poster should reflect a welcoming, casual, but also elegant establishment. Images of food and the venue can be found here https://www.copperfernsmokehouse.com/

Target Market(s)

18 to 65, broad range of people, local restaurant, people popping in for a quick bite, and also celebrating main events

Industry/Entity Type

Restaurant

Font styles to use
Sans Serif

Colors
0054AA
0677BA
7BADD7
CADEEF
E8F1F8
EB3D1F
EC4F4E
F09395
F8D3D4
FCEDEE

Requirements
Must have
• Each poster must contain the text that is in the attached draft poster, illustration
Nice to have
• Colours similar to what is in attached file, though open to other otions

```html
<!DOCTYPE html>
<html lang="en">
<head>
<meta charset="utf-8">
<title>Copperfern Smokehouse – Tuesday Special</title>
<link href="https://fonts.googleapis.com/css2?family=Montserrat:wght@700&family=Oswald:wght@700&display=swap" rel="stylesheet">
<style>
  :root {
    --page-bg: #e8f1f8;
    --navy: #0a2544;
    --blue-deep: #0054aa;
    --blue-mid: #0677ba;
    --blue-soft: #7badd7;
    --blue-pale: #cadeef;
    --blue-mist: #e8f1f8;
    --red-hot: #eb3d1f;
    --red-warm: #ec4f4e;
    --pink: #f09395;
    --pink-pale: #f8d3d4;
  }
  html, body {
    margin: 0;
    width: 1200px;
    height: 1200px;
    overflow: hidden;
    background: var(--page-bg);
  }
  .poster {
    position: absolute;
    left: 225px;
    top: 70px;
    width: 750px;
    height: 1060px;
    background: var(--navy);
    overflow: hidden;
    font-family: "Montserrat", sans-serif;
  }
  .hero-illustration {
    position: absolute;
    left: 0; top: 0;
    width: 750px;
    height: 612px;
    background:
      radial-gradient(ellipse 38% 30% at 30% 30%, var(--red-warm), transparent 72%),
      radial-gradient(ellipse 45% 26% at 72% 38%, var(--red-hot), transparent 75%),
      radial-gradient(ellipse 70% 28% at 50% 62%, var(--pink), transparent 80%),
      linear-gradient(180deg, var(--blue-deep) 0%, var(--blue-mid) 30%, #8a3a4a 60%, var(--navy) 100%);
  }
  .brand-badge {
    position: absolute;
    left: 311px;
    top: 504px;
    width: 150px;
    height: 150px;
    border-radius: 50%;
    background: var(--navy);
    display: flex;
    align-items: center;
    justify-content: center;
    text-align: center;
  }
  .brand-name {
    color: var(--blue-mist);
    font-weight: 700;
    font-size: 13px;
    line-height: 1.35;
    letter-spacing: 2px;
  }
  .headline {
    position: absolute;
    left: 0; width: 100%;
    text-align: center;
    margin: 0;
    line-height: 1;
  }
  .special-title {
    top: 683px;
    font-family: "Oswald", sans-serif;
    font-weight: 700;
    font-size: 48px;
    letter-spacing: 1px;
    color: var(--blue-mist);
  }
  .special-price {
    top: 740px;
    font-size: 37px;
    font-weight: 700;
    color: var(--pink);
  }
  .contact-rule {
    position: absolute;
    left: 0; top: 830px;
    width: 100%;
    height: 15px;
    background: var(--blue-mist);
  }
  .contact-label {
    position: absolute;
    left: 271px; top: 805px;
    width: 208px; height: 64px;
    background: var(--blue-mist);
    color: var(--navy);
    font-family: "Oswald", sans-serif;
    font-weight: 700;
    font-size: 40px;
    letter-spacing: 1px;
    display: flex;
    align-items: center;
    justify-content: center;
  }
  .contact-list {
    position: absolute;
    left: 0; top: 896px;
    width: 100%;
    margin: 0; padding: 0;
    list-style: none;
    text-align: center;
    color: var(--blue-pale);
    font-weight: 700;
    font-size: 19px;
    line-height: 20px;
  }
  .contact-list li { height: 42.5px; }
</style>
</head>
<body>
  <main class="poster">
    <div class="hero-illustration" role="img" aria-label="Illustration of meat cooking over flames on a barbecue grill"></div>
    <div class="brand-badge">
      <span class="brand-name">COPPERFERN<br>SMOKEHOUSE</span>
    </div>
    <h1 class="headline special-title">TUESDAY SPECIAL</h1>
    <p class="headline special-price">$25 PER PERSON</p>
    <div class="contact-rule"></div>
    <div class="contact-label">CONTACT</div>
    <ul class="contact-list">
      <li>218 HARLOW STREET, EASTMERE</li>
      <li>0400 555 217</li>
      <li>HELLO@COPPERFERNSMOKEHOUSE.COM</li>
    </ul>
  </main>
</body>
</html>
```